website for Velunora.de

In Naturheilzentrum VELUNORA, the medical team using the Advanced Laboratory examines the health status of patients and each patient is treated with special care in Germany. Multi language.
The design must show mix of modern medical service.
pages :
1. Home
2. Philosophie
3.Diagnose
4. Therapie
5. Kontakt
6.über uns
7. Zentrum ( Bilder )
8.Unser Ergebnisse
9. Anfahrt

Target Market(s)

International

Industry/Entity Type

Hospital

Font styles to use
Decorative

Colors
0455a3

Requirements
Must have
• The design must show mix of modern medical service.
• Advanced Laboratory abilities.
Nice to have
• Medical Theme
• for blue color reference see the attachment 1.jpeg

```html
<!DOCTYPE html>
<html lang="en">
<head>
<meta charset="utf-8">
<title>Velunora – Naturheilzentrum</title>
<link href="https://fonts.googleapis.com/css2?family=Poppins:wght@300;400;500;600;700&display=swap" rel="stylesheet">
<style>
:root{
  --blue:#0455a3;
  --blue-bright:#1a80f0;
  --navy:#0b1a2f;
  --navy-deep:#06111f;
  --ink:#1d2b3a;
  --grey:#7b8794;
  --light:#f4f6f9;
  --red:#e0262f;
  --green:#7cc142;
  --white:#ffffff;
}
*{box-sizing:border-box;margin:0;padding:0}
html,body{width:1200px;height:3930px;overflow:hidden}
body{position:relative;background:var(--white);font-family:"Poppins",Arial,sans-serif;color:var(--ink)}
.abs{position:absolute}

/* Header & hero */
.hero{left:0;top:0;width:1200px;height:676px;background:linear-gradient(135deg,#c9d8e6 0%,#9fb6cc 45%,#5e7f9f 100%);overflow:hidden}
.hero-curve{left:0;top:0}
.brand{left:26px;top:30px;display:flex;align-items:center;gap:10px;font-weight:600;font-size:30px;color:var(--blue);letter-spacing:1px}
.brand-dot{width:22px;height:22px;border-radius:50%;background:var(--red)}
.nav{left:360px;top:40px;display:flex;gap:26px;align-items:center;font-size:14px;color:var(--white)}
.nav .active{color:var(--red)}
.nav .flag{width:22px;height:14px;background:#d7dde4}
.hero-circle{left:160px;top:132px;width:392px;height:392px;border-radius:50%;background:rgba(10,95,190,.82)}
.hero-copy{left:190px;top:215px;width:330px;text-align:center;color:var(--white)}
.hero-title{font-size:33px;font-weight:400;line-height:1.2;letter-spacing:.5px}
.hero-title .hl-red{color:var(--red);font-weight:600}
.hero-title .hl-green{color:var(--green);font-weight:600}
.hero-text{margin-top:22px;font-size:11px;line-height:1.75;opacity:.9}
.hero-btn{display:inline-block;margin-top:28px;border:1px solid var(--white);padding:6px 20px;font-size:12px;font-weight:500}
.hero-notch{left:578px;top:648px}

/* Welcome */
.welcome-img{left:112px;top:798px}
.welcome-copy{left:590px;top:845px;width:432px}
.eyebrow{font-size:17px;color:var(--blue);letter-spacing:1px}
.welcome-title{font-size:58px;color:var(--blue);font-weight:400;line-height:1.1}
.welcome-title b{font-weight:700}
.welcome-rule{left:528px;top:962px;width:66px;height:2px;background:var(--blue)}
.welcome-text{margin-top:26px;font-size:11.5px;line-height:2.05;color:var(--grey)}
.read-more{margin-top:22px;font-size:13px;color:var(--blue);display:flex;align-items:center;gap:6px}

/* Featured hospital */
.featured-bg{left:0;top:1433px;width:686px;height:755px;background:var(--light)}
.featured-photo{left:686px;top:1433px;width:514px;height:750px;background:linear-gradient(180deg,#b9cbe0 0%,#6d8fb9 45%,#1a3f73 80%,#0b1f3d 100%)}
.featured-copy{left:170px;top:1513px}
.featured-title{font-size:40px;color:var(--blue);font-weight:400;letter-spacing:.5px}
.featured-title b{font-weight:700}
.featured-rule{left:118px;top:1643px;width:104px;height:2px;background:var(--blue)}
.hospital-list{left:170px;top:1690px;list-style:none;font-size:22px;color:var(--ink);line-height:60px;letter-spacing:.3px}

/* Offer slider */
.offer-block{left:0;top:2183px;width:118px;height:385px;background:var(--blue)}
.offer-photo{left:118px;top:1980px;width:864px;height:588px;background:linear-gradient(120deg,#dfe6ec 0%,#c9d6e0 40%,#e6d7c9 75%,#c7d5d9 100%)}
.offer-box{left:550px;top:2280px;width:432px;height:288px;background:var(--blue);color:var(--white);padding:40px 34px}
.offer-title{font-size:30px;font-weight:400;line-height:1.45;letter-spacing:.5px}
.offer-rule{left:440px;top:2423px;width:110px;height:2px;background:var(--blue)}
.offer-text{margin-top:34px;font-size:11.5px;line-height:2.1;opacity:.9}
.slider-dot{width:36px;height:36px;border-radius:50%;border:1.5px solid var(--white);display:flex;align-items:center;justify-content:center}

/* Doctors */
.doctors-head{left:0;top:2610px;width:1200px;text-align:center;color:var(--blue)}
.doctors-title{font-size:52px;font-weight:400;letter-spacing:1px;line-height:1.15}
.doctors-title b{font-weight:700}
.doctor{top:2740px;width:197px}
.doctor-photo{height:268px;background:linear-gradient(180deg,#e9eef3 0%,#c8d6e3 100%)}
.doctor-info{height:125px;background:var(--blue);color:var(--white);padding:14px 14px}
.doctor-role{font-size:11px;opacity:.85}
.doctor-name{font-size:17px;font-weight:600;margin-top:1px}
.doctor-text{font-size:10.5px;line-height:1.6;margin-top:6px;opacity:.85}
.doctor-social{display:flex;gap:4px;justify-content:flex-end;margin-top:6px}
.doctor-social span{width:14px;height:14px;border:1px solid var(--white)}
.doctor-arrows{left:556px;top:3154px}

/* Testimonial & footer */
.footer{left:0;top:3471px;width:1200px;height:459px;background:var(--navy)}
.testimonial{left:0;top:3246px;width:998px;height:307px;background:var(--blue-bright);color:var(--white);text-align:center}
.avatar{left:467px;top:3289px;width:64px;height:64px;border-radius:50%;background:linear-gradient(135deg,#e8c9a6,#a9785a);border:3px solid var(--white)}
.quote{left:230px;top:3372px;width:540px;font-size:12.5px;line-height:1.9;color:var(--white);text-align:center}
.quote-name{left:0;top:3442px;width:998px;text-align:center;color:var(--white);font-size:26px;font-weight:700;letter-spacing:1px}
.quote-role{left:0;top:3478px;width:998px;text-align:center;color:var(--white);font-size:13px;letter-spacing:1px}
.quote-dots{left:926px;top:3356px;display:flex;flex-direction:column;gap:10px}
.quote-dots span{width:5px;height:5px;border-radius:50%;background:var(--white);opacity:.6}
.quote-dots span:first-child{opacity:1}

.col-title{font-size:13px;font-weight:600;color:var(--white);letter-spacing:.5px}
.hours{left:173px;top:3643px;width:250px}
.hours-row{display:flex;justify-content:space-between;font-size:11.5px;color:#c7d0db;margin-top:26px}
.contact{left:466px;top:3643px;width:260px}
.contact-row{display:flex;gap:10px;align-items:flex-start;font-size:11.5px;color:#c7d0db;line-height:1.5;margin-top:22px}
.contact-row svg{flex:none;margin-top:2px}
.form{left:757px;top:3643px;width:230px}
.form-field{font-size:11.5px;line-height:16px;color:#c7d0db;border-bottom:1px solid #3b4b60;padding-bottom:6px;margin-top:13px}
.form-btn{display:inline-block;margin-top:16px;background:var(--white);color:var(--navy);font-size:11px;line-height:16px;font-weight:600;padding:3px 22px}
.copyright{left:0;top:3880px;width:1200px;height:50px;background:var(--navy-deep);color:#aab4c0;font-size:11.5px;display:flex;align-items:center;justify-content:center}
</style>
</head>
<body>

<header>
  <div class="abs hero" role="img" aria-label="Photo: nurse in blue uniform assisting an elderly patient in a wheelchair along a bright hospital corridor"></div>
  <svg class="abs hero-curve" width="1200" height="200" viewBox="0 0 1200 200" aria-hidden="true">
    <path d="M0 0 H420 C300 40 130 100 0 180 Z" fill="#ffffff"/>
    <path d="M0 180 C130 100 300 40 420 0" fill="none" stroke="#0455a3" stroke-width="3"/>
  </svg>
  <div class="abs brand"><span class="brand-dot"></span>VELUNORA</div>
  <nav class="abs nav">
    <span class="active">Home</span><span>About us</span><span>Philosophy</span><span>diagnosis</span><span>therapy</span><span>Our results</span><span>approach</span><span>Contact</span>
    <svg width="14" height="14" viewBox="0 0 14 14" aria-hidden="true"><circle cx="6" cy="6" r="4.5" fill="none" stroke="#fff" stroke-width="1.5"/><line x1="9.5" y1="9.5" x2="13" y2="13" stroke="#fff" stroke-width="1.5"/></svg>
    <span class="flag" aria-label="Language"></span>
  </nav>
  <div class="abs hero-circle"></div>
  <div class="abs hero-copy">
    <h1 class="hero-title">FIND <span class="hl-red">YOUR</span> WAY<br>TO THE <span class="hl-green">BEST</span> CARE</h1>
    <p class="hero-text">Lorem ipsum dolor sit amet, consectetur adipiscing elit. Sed luctus turpis eu eget tempor eleifend sagittis erat. In hac habitasse platea dictumst. Duis nec consectetur tellus nam condimentum gravida leo tempor sodales. Proin magna diam.</p>
    <span class="hero-btn">FIND OUT MORE</span>
  </div>
  <svg class="abs hero-notch" width="48" height="28" viewBox="0 0 48 28" aria-hidden="true"><path d="M0 28 L24 4 L48 28 Z" fill="#0455a3"/><path d="M19 18 L24 13 L29 18" fill="none" stroke="#fff" stroke-width="1.5"/></svg>
</header>

<section class="welcome">
  <svg class="abs welcome-img" width="420" height="424" viewBox="0 0 420 424" role="img" aria-label="Photo: smiling female doctor with stethoscope holding a clipboard, framed in a cross shape">
    <defs><linearGradient id="welcomeFill" x1="0" y1="0" x2="1" y2="1"><stop offset="0" stop-color="#eef2f6"/><stop offset="1" stop-color="#cfdbe7"/></linearGradient></defs>
    <path d="M145 14 H275 Q287 14 287 26 V137 H398 Q410 137 410 149 V275 Q410 287 398 287 H287 V398 Q287 410 275 410 H145 Q133 410 133 398 V287 H22 Q10 287 10 275 V149 Q10 137 22 137 H133 V26 Q133 14 145 14 Z" fill="url(#welcomeFill)"/>
    <path d="M10 200 V275 Q10 287 22 287 H133 V398 Q133 410 145 410 H287" fill="none" stroke="#0455a3" stroke-width="5"/>
  </svg>
  <div class="abs welcome-rule"></div>
  <div class="abs welcome-copy">
    <p class="eyebrow">WELCOME</p>
    <h2 class="welcome-title"><b>VELUNORA</b></h2>
    <p class="welcome-text">Lorem ipsum dolor sit amet, consectetur adipiscing elit. Quisque sed dolor finibus, aliquet tellus in, bibendum justo. Etiam vel risus et lectus suscipit euismod. Vivamus porta lacus ut augue facilisis imperdiet. Vivamus mollis est non mi eu fermentum tempor tellus porta. Morbi dolor ex, vestibulum sed ligula at, finibus vehicula risus. Etiam dictum fermentum eros, quis commodo elit mollis a. Fusce massa orci, scelerisque quis mi at, gravida porttitor eros.</p>
    <p class="read-more">READ MORE <svg width="14" height="10" viewBox="0 0 14 10" aria-hidden="true"><path d="M0 5 H12 M8 1 L12 5 L8 9" fill="none" stroke="#0455a3" stroke-width="1.5"/></svg></p>
  </div>
</section>

<section class="featured">
  <div class="abs featured-bg"></div>
  <div class="abs featured-photo" role="img" aria-label="Photo: team of doctors and nurses in a hospital, under a blue tint"></div>
  <div class="abs featured-copy">
    <p class="eyebrow">OUR</p>
    <h2 class="featured-title"><b>FEATURED</b> HOSPITAL</h2>
  </div>
  <div class="abs featured-rule"></div>
  <ul class="abs hospital-list">
    <li>BROOKMERE HOSPITAL</li>
    <li>ELMWOOD MEDICAL CENTER</li>
    <li>LINDEN HILL HOSPITAL</li>
    <li>HARBORVIEW CLINIC</li>
  </ul>
</section>

<section class="offer">
  <div class="abs offer-block"></div>
  <div class="abs offer-photo" role="img" aria-label="Photo: doctors and dental staff in discussion in a bright clinic"></div>
  <div class="abs slider-dot" style="left:100px;top:2327px"><svg width="10" height="10" viewBox="0 0 10 10" aria-hidden="true"><path d="M7 1 L3 5 L7 9" fill="none" stroke="#fff" stroke-width="1.5"/></svg></div>
  <div class="abs slider-dot" style="left:100px;top:2374px"><svg width="10" height="10" viewBox="0 0 10 10" aria-hidden="true"><path d="M3 1 L7 5 L3 9" fill="none" stroke="#fff" stroke-width="1.5"/></svg></div>
  <div class="abs offer-box">
    <h3 class="offer-title">20% DISCOUNT ON TEETH WHITENING</h3>
    <p class="offer-text">Lorem ipsum dolor sit amet, consectetur adipiscing elit. Sed non turpis posuere, volutpat elit vel, rutrum ligula. Cras eget volutpat urna. Phasellus id dolor ornare, fringilla enim id, vestibulum dolor.</p>
  </div>
  <div class="abs offer-rule"></div>
</section>

<section class="doctors">
  <div class="abs doctors-head">
    <p class="eyebrow">OUR</p>
    <h2 class="doctors-title">DOCTORS <b>TEAM</b></h2>
  </div>
  <article class="abs doctor" style="left:173px">
    <div class="doctor-photo" role="img" aria-label="Photo: female dental surgeon in white coat"></div>
    <div class="doctor-info"><p class="doctor-role">Dental Surgeon</p><p class="doctor-name">Clara Wendt</p><p class="doctor-text">Lorem ipsum dolor sit amet, consectetur adipiscing elit.</p><div class="doctor-social"><span></span><span></span><span></span></div></div>
  </article>
  <article class="abs doctor" style="left:393px">
    <div class="doctor-photo" role="img" aria-label="Photo: female dentist in blue scrubs"></div>
    <div class="doctor-info"><p class="doctor-role">Dentist</p><p class="doctor-name">Lena Morrow</p><p class="doctor-text">Lorem ipsum dolor sit amet, consectetur adipiscing elit.</p><div class="doctor-social"><span></span><span></span><span></span></div></div>
  </article>
  <article class="abs doctor" style="left:613px">
    <div class="doctor-photo" role="img" aria-label="Photo: female dental surgeon with stethoscope"></div>
    <div class="doctor-info"><p class="doctor-role">Dental Surgeon</p><p class="doctor-name">Ida Fairbank</p><p class="doctor-text">Lorem ipsum dolor sit amet, consectetur adipiscing elit.</p><div class="doctor-social"><span></span><span></span><span></span></div></div>
  </article>
  <article class="abs doctor" style="left:833px">
    <div class="doctor-photo" role="img" aria-label="Photo: female dental surgeon with glasses and red stethoscope"></div>
    <div class="doctor-info"><p class="doctor-role">Dental Surgeon</p><p class="doctor-name">Nora Castell</p><p class="doctor-text">Lorem ipsum dolor sit amet, consectetur adipiscing elit.</p><div class="doctor-social"><span></span><span></span><span></span></div></div>
  </article>
  <svg class="abs doctor-arrows" width="90" height="22" viewBox="0 0 90 22" aria-hidden="true">
    <path d="M38 11 H2 M8 5 L2 11 L8 17" fill="none" stroke="#9aa6b2" stroke-width="1.5"/>
    <path d="M52 11 H88 M82 5 L88 11 L82 17" fill="none" stroke="#0455a3" stroke-width="1.5"/>
  </svg>
</section>

<footer>
  <div class="abs footer"></div>
  <div class="abs testimonial"></div>
  <div class="abs avatar" role="img" aria-label="Portrait photo of the reviewer"></div>
  <p class="abs quote">It is such a great feeling to know that our family has found a child care that is so loving and supportive. LittleNest has given our children excellent care! Their babysitters are so wonderful and encouraging to our family.</p>
  <p class="abs quote-name">RASMUSSEN</p>
  <p class="abs quote-role">PURCHASER</p>
  <div class="abs quote-dots"><span></span><span></span><span></span></div>

  <div class="abs hours">
    <p class="col-title">WORKING HOURS</p>
    <div class="hours-row"><span>MON – WED</span><span>8:00 AM – 7:00 PM</span></div>
    <div class="hours-row"><span>THU</span><span>8:00 AM – 5:00 PM</span></div>
    <div class="hours-row"><span>FRI</span><span>8:00 AM – 5:00 PM</span></div>
    <div class="hours-row"><span>SAT – SUN</span><span>Closed</span></div>
  </div>

  <div class="abs contact">
    <p class="col-title">CONTACT US</p>
    <div class="contact-row"><svg width="12" height="14" viewBox="0 0 12 14" aria-hidden="true"><path d="M6 13 C2 8 1 6.5 1 5 A5 5 0 0 1 11 5 C11 6.5 10 8 6 13 Z" fill="#e0262f"/><circle cx="6" cy="5" r="1.8" fill="#0b1a2f"/></svg><span>12 LINDENWEG, SUITE 40<br>VELDEN, VL 2041</span></div>
    <div class="contact-row"><svg width="12" height="12" viewBox="0 0 12 12" aria-hidden="true"><path d="M2 1 L4.5 1 L5.5 3.5 L4 4.8 C4.8 6.5 5.5 7.2 7.2 8 L8.5 6.5 L11 7.5 L11 10 C11 10.6 10.6 11 10 11 C5 11 1 7 1 2 C1 1.4 1.4 1 2 1 Z" fill="#e0262f"/></svg><span>Tel : (00) 555-0142</span></div>
    <div class="contact-row"><svg width="13" height="10" viewBox="0 0 13 10" aria-hidden="true"><rect x="0.5" y="0.5" width="12" height="9" fill="#e0262f"/><path d="M0.5 0.5 L6.5 5.5 L12.5 0.5" fill="none" stroke="#0b1a2f" stroke-width="1"/></svg><span>Email : INFO@VELUNORA.DE</span></div>
  </div>

  <div class="abs form">
    <p class="col-title">APARTMENT FROM</p>
    <p class="form-field">Name</p>
    <p class="form-field">Email</p>
    <p class="form-field">Phone</p>
    <p class="form-field">Doctor</p>
    <span class="form-btn">SUBMIT</span>
  </div>

  <div class="abs copyright">© Copyright 2018 Velunora.de</div>
</footer>

</body>
</html>
```